Etiketten für Honigwein
Zielgruppe
Wir sind eine kleine Metmanufaktur im Süden des Schwarzwalds und haben uns auf den Namen
Tarquil getauft. Bei unseren Produkten setzen wir auf Qualität statt auf Quantität. Zu unserer
Zielgruppe gehören exklusive Schlossrestaurants, Gaststätten in antikem oder mittelalterlichen
Ambiente sowie Mittelaltermärkte. Später soll diese auf Feinkostläden und auch den Getränkehandel
erweitert werden.
Aufgabenstellung
Siehe angehängtes PDF.
Falls ein Designer eine bessere Idee zu manchen Punkten oder dem gesamten Design hat, sind wir gerne bereit, uns von diesen inspirieren zu lassen.
Posivitbeispiele sind mit Positiv1, Positiv2, etc. und Negativbeispiele mit Negativ1, Negativ2, etc. beschriftet.

```html
<!DOCTYPE html>
<html lang="de">
<head>
<meta charset="utf-8">
<title>Tarquil – Kirsch-Met Etikett</title>
<link rel="stylesheet" href="https://fonts.googleapis.com/css2?family=Josefin+Sans:wght@400;600&display=swap">
<style>
  :root {
    --backdrop: #1c1a1f;
    --label-black: #121113;
    --label-edge: #2a282c;
    --silver: #e4e4e8;
    --silver-dim: #bdbdc3;
    --cherry: #e0645c;
    --cherry-deep: #b83c3c;
    --honey: #f0a050;
    --forest: #6e2a4a;
    --forest-dark: #3a1526;
  }
  * { box-sizing: border-box; margin: 0; padding: 0; }
  html, body { width: 900px; height: 1200px; overflow: hidden; }
  body {
    background: var(--backdrop);
    font-family: "Josefin Sans", sans-serif;
    color: var(--silver);
  }
  .label {
    position: absolute;
    left: 160px;
    top: 80px;
    width: 580px;
    height: 1040px;
    background: var(--label-black);
    border: 1px solid var(--label-edge);
    overflow: hidden;
  }
  .brand {
    position: absolute;
    top: 190px;
    left: 30px;
    right: 30px;
  }
  .brand-name {
    font-weight: 600;
    font-size: 96px;
    letter-spacing: 6px;
    text-transform: uppercase;
    line-height: 1;
    text-align: center;
    color: var(--silver);
  }
  .brand-rule {
    height: 3px;
    background: var(--silver-dim);
    margin: 10px 0 8px;
  }
  .brand-sub {
    text-align: right;
    font-weight: 400;
    font-size: 24px;
    letter-spacing: 4px;
    color: var(--silver-dim);
  }
  .illustration {
    position: absolute;
    top: 400px;
    left: 40px;
    width: 500px;
    height: 360px;
    background:
      radial-gradient(closest-side at 72% 30%, rgba(240,160,80,0.35), rgba(240,160,80,0) 100%),
      radial-gradient(closest-side at 42% 68%, rgba(224,100,92,0.75), rgba(184,60,60,0.35) 55%, rgba(18,17,19,0) 100%);
  }
  .variety {
    position: absolute;
    top: 790px;
    width: 100%;
    text-align: center;
    font-weight: 600;
    font-size: 24px;
    letter-spacing: 1px;
    color: var(--cherry);
  }
  .forest-band {
    position: absolute;
    left: 0;
    bottom: 0;
    width: 100%;
    height: 190px;
    background: linear-gradient(to bottom, rgba(110,42,74,0) 0%, rgba(110,42,74,0.7) 45%, var(--forest) 70%, var(--forest-dark) 100%);
  }
  .vintage {
    position: absolute;
    top: 900px;
    width: 100%;
    text-align: center;
    line-height: 1.15;
  }
  .vintage-type {
    font-weight: 600;
    font-size: 24px;
    letter-spacing: 1px;
    color: var(--silver);
  }
  .vintage-year {
    font-weight: 400;
    font-size: 24px;
    color: var(--silver);
  }
</style>
</head>
<body>
  <main class="label">
    <header class="brand">
      <div class="brand-name">Tarquil</div>
      <div class="brand-rule"></div>
      <div class="brand-sub">SCHWARZWÄLDER MET</div>
    </header>

    <div class="illustration" role="img" aria-label="Linienzeichnung: zwei rote Kirschen an Stielen auf einer welligen Hügellinie, daneben ein Honigglas mit Honiglöffel"></div>

    <p class="variety">KIRSCH-MET</p>

    <div class="forest-band" role="img" aria-label="Silhouette eines Tannenwaldes in Beerentönen am unteren Etikettrand"></div>

    <div class="vintage">
      <p class="vintage-type">HONIGWEIN</p>
      <p class="vintage-year">2022</p>
    </div>
  </main>
</body>
</html>
```